Harbor Crest Residential Business Card Design - Logo Provided

business card design - LOGO PROVIDED. private capital fund investing in: commercial real estate (apartments), asset backed lending, private credit, flexible capital

Target Market(s)

private capital: commercial real estate (apartments), asset backed lending, private credit, flexible capital

Industry/Entity Type

alternative asset management

Contact Information for Business Card

logo, name, title, phone number, email and website

Font styles to use
Sans Serif

Colors
0054AA
0677BA
7BADD7
CADEEF
E8F1F8
EB3D1F
EC4F4E
F09395
F8D3D4
FCEDEE

Requirements
Must have
• use of logo on both sides and a qr code on the back

```html
<!DOCTYPE html>
<html lang="en">
<head>
<meta charset="utf-8">
<title>Harbor Crest Residential – Business Card</title>
<link href="https://fonts.googleapis.com/css2?family=Arimo:wght@400;700&display=swap" rel="stylesheet">
<style>
  :root{
    --stage:#a3a3a3;
    --navy:#16254a;
    --navy-deep:#11203b;
    --stripe:#1a2a52;
    --red:#df2027;
    --red-dark:#9e1a20;
    --white:#ffffff;
    --paper:#f8f6fa;
  }
  *{box-sizing:border-box;margin:0;padding:0}
  html,body{width:1200px;height:1200px;overflow:hidden;background:var(--stage);font-family:"Arimo",Arial,sans-serif}
  .card{position:absolute;left:179px;width:852px;height:530px;border-radius:26px;background:var(--navy);overflow:hidden;box-shadow:0 2px 6px rgba(0,0,0,.25)}
  .card--front{top:55px}
  .card--back{top:618px}
  .stripes{position:absolute;background:repeating-linear-gradient(to bottom,var(--navy-deep) 0 22px,var(--stripe) 22px 29px)}
  .front-stripes{left:0;top:0;width:852px;height:280px}
  .logo-column{position:absolute;left:315px;top:0;width:217px;height:221px;background:var(--navy)}
  .brand{position:absolute;display:flex;align-items:center;gap:10px;font-weight:700;line-height:1.05}
  .brand-mark{flex:none;background:var(--red)}
  .brand--front{left:315px;top:0;width:217px;height:221px;justify-content:center;color:var(--white);font-size:19px}
  .brand--front .brand-mark{width:22px;height:22px}
  .tagline{position:absolute;left:0;right:0;top:311px;padding-left:56px;text-align:center;color:var(--white);font-weight:700;font-size:21px;letter-spacing:.2px}
  .focus-band{position:absolute;left:0;top:420px;width:852px;height:75px;background:var(--navy-deep)}
  .focus{position:absolute;top:373px;width:186px;height:122px;background:var(--red);color:var(--white);font-size:21px;text-align:center;line-height:1.1;display:flex;align-items:flex-end;justify-content:center;padding-bottom:12px}
  .focus-tab{position:absolute;left:49px;top:0;width:79px;height:54px;background:var(--navy-deep);border-radius:0 0 5px 5px;display:flex;align-items:center;justify-content:center}
  .focus-tab svg{width:38px;height:38px}
  .back-top{left:0;top:0;width:852px;height:75px}
  .back-left{left:0;top:75px;width:308px;height:378px}
  .name-banner{position:absolute;left:0;top:124px;width:322px;height:81px;background:var(--red);color:var(--white);font-weight:700;font-size:29px;line-height:1.05;padding:12px 0 0 15px}
  .name-banner::after{content:"";position:absolute;right:-12px;top:-12px;width:12px;height:105px;background:var(--red-dark);clip-path:polygon(0 0,100% 12%,100% 88%,0 100%)}
  .logo-panel{position:absolute;left:15px;top:206px;width:245px;height:183px;background:var(--paper);border-radius:0 0 12px 12px;display:flex;align-items:center;justify-content:center}
  .brand--back{position:static;color:var(--navy);font-size:21px}
  .brand--back .brand-mark{width:24px;height:24px}
  .contact-icon{position:absolute;width:65px;height:64px;background:var(--red);border-radius:5px;display:flex;align-items:center;justify-content:center}
  .contact-icon svg{width:38px;height:38px}
  .contact-bar{position:absolute;right:0;height:64px;background:var(--red);border-radius:5px 0 0 5px;color:var(--white);font-size:22px;display:flex;align-items:center;padding-left:19px}
</style>
</head>
<body>

<section class="card card--front">
  <div class="stripes front-stripes"></div>
  <div class="logo-column"></div>
  <div class="brand brand--front"><span class="brand-mark"></span><span>HARBOR CREST<br>RESIDENTIAL</span></div>

  <h2 class="tagline">PRIVATE CAPITAL FUND INVESTING IN</h2>
  <div class="focus-band"></div>

  <div class="focus" style="left:30px">
    <div class="focus-tab"><svg viewBox="0 0 40 40" fill="#fff"><rect x="8" y="6" width="12" height="30"/><rect x="20" y="3" width="8" height="33"/><path d="M22 26l8-6 8 6v10H22z"/><g fill="#11203b"><rect x="10" y="10" width="2" height="3"/><rect x="15" y="10" width="2" height="3"/><rect x="10" y="17" width="2" height="3"/><rect x="15" y="17" width="2" height="3"/><rect x="10" y="24" width="2" height="3"/><rect x="28" y="30" width="4" height="6"/></g></svg></div>
    <span>Commercial<br>real estate</span>
  </div>
  <div class="focus" style="left:235px">
    <div class="focus-tab"><svg viewBox="0 0 40 40" fill="none" stroke="#fff" stroke-width="2.5"><circle cx="22" cy="12" r="8"/><path d="M4 28c6-4 10-4 14-2h8c2 0 2 3 0 3h-8M4 34l6-2 12 2 14-8"/><text x="22" y="16" fill="#fff" stroke="none" font-size="11" font-family="Arimo,sans-serif" text-anchor="middle" font-weight="700">$</text></svg></div>
    <span>Asset backed<br>lending</span>
  </div>
  <div class="focus" style="left:440px">
    <div class="focus-tab"><svg viewBox="0 0 40 40"><rect x="3" y="8" width="28" height="20" rx="3" fill="#fff"/><rect x="3" y="13" width="28" height="3" fill="#11203b"/><rect x="20" y="20" width="15" height="14" rx="2" fill="#fff" stroke="#11203b" stroke-width="1.5"/><path d="M23 20v-4a4.5 4.5 0 0 1 9 0v4" fill="none" stroke="#fff" stroke-width="2.5"/><circle cx="27.5" cy="27" r="2" fill="#11203b"/></svg></div>
    <span>Private credit</span>
  </div>
  <div class="focus" style="left:645px">
    <div class="focus-tab"><svg viewBox="0 0 40 40" fill="none" stroke="#fff" stroke-width="2.5"><path d="M8 12a15 15 0 0 1 24 0M32 28a15 15 0 0 1-24 0"/><circle cx="20" cy="20" r="8" fill="#fff" stroke="none"/><text x="20" y="24" fill="#11203b" font-size="11" font-family="Arimo,sans-serif" text-anchor="middle" font-weight="700" stroke="none">$</text></svg></div>
    <span>Flexible Capital</span>
  </div>
</section>

<section class="card card--back">
  <div class="stripes back-top"></div>
  <div class="stripes back-left"></div>

  <div class="name-banner">HARBOR CREST<br>RESIDENTIAL</div>
  <div class="logo-panel">
    <div class="brand brand--back"><span class="brand-mark"></span><span>HARBOR CREST<br>RESIDENTIAL</span></div>
  </div>

  <div class="contact-icon" style="left:390px;top:122px"><svg viewBox="0 0 40 40" fill="none" stroke="#fff" stroke-width="2.5"><path d="M5 16v18h30V16L20 5z"/><path d="M5 34l12-10M35 34L23 24M5 16l15 11 15-11"/><text x="20" y="21" fill="#fff" stroke="none" font-size="11" font-family="Arimo,sans-serif" text-anchor="middle" font-weight="700">@</text></svg></div>
  <div class="contact-bar" style="left:462px;top:122px">info@harborcrest.com</div>

  <div class="contact-icon" style="left:390px;top:196px"><svg viewBox="0 0 40 40" fill="#fff"><path d="M4 14c0-5 32-5 32 0v3h-8v-3c-4-2-12-2-16 0v3H4z"/><path d="M10 20h20l4 14H6z"/></svg></div>
  <div class="contact-bar" style="left:462px;top:196px;padding-left:24px">2-555-014-2388</div>

  <div class="contact-icon" style="left:390px;top:269px"><svg viewBox="0 0 40 40" fill="none" stroke="#fff" stroke-width="2.5"><circle cx="19" cy="20" r="14"/><ellipse cx="19" cy="20" rx="6" ry="14"/><path d="M5 20h28M8 12h22M8 28h22"/></svg></div>
  <div class="contact-bar" style="left:462px;top:269px;padding-left:24px">www.websiteaddress.com</div>

  <div class="contact-icon" style="left:277px;top:341px"><svg viewBox="0 0 40 40" fill="#fff"><path d="M20 4a11 11 0 0 1 11 11c0 8-11 19-11 19S9 23 9 15A11 11 0 0 1 20 4z"/><circle cx="20" cy="15" r="4" fill="#df2027"/><rect x="14" y="35" width="12" height="2.5" rx="1"/></svg></div>
  <div class="contact-bar" style="left:348px;top:341px">Street Address Here Loremipsum. 22222</div>
</section>

</body>
</html>
```